Home Health Care Agency Needs a Website (Seeking a PSD)

We need a user friendly website for a Home Health Care Agency. Our service is for the elderly and disabled. Frequently the busy professional middle-aged married daughter will use the website to arrange in-home care for an aging parent. Therefore, our website is primarily geared towards middle-aged women. In-home care is typically 24 hours a day so, a feeling of trustworthiness and security should be effectively conveyed. (Seeking a PSD- however, if you also offer coding, please let us know the cost.)

Target Market(s)

Frequently the busy professional middle-aged married daughter (possibly out of state) will use the website to arrange in-home care for an aging parent.

Industry/Entity Type

Security

Requirements
Must have
• Website must be clean, uncluttered and professional. The following menu pages are requested: Home, About Us, Services, Resources, FAQ, Employment & Contact.
Should not have
• Must not be too whimsical.

```html
<!DOCTYPE html>
<html lang="en">
<head>
<meta charset="utf-8">
<title>Meadowlane Home Health</title>
<link href="https://fonts.googleapis.com/css2?family=Open+Sans:wght@300;400;600;700&family=Roboto:wght@300;400;500&display=swap" rel="stylesheet">
<style>
  :root{
    --sky:#4bc8ef;
    --ink:#2f2e33;
    --text:#555;
    --muted:#8a8a8a;
    --nav-bg:#f2f2f2;
    --btn:#5b5b5b;
    --white:#fff;
    --green-1:#6aa53a;
    --green-2:#4e8a2b;
    --skin:#d9a08f;
  }
  *{box-sizing:border-box;margin:0;padding:0}
  html,body{width:1018px;height:1200px;overflow:hidden;background:var(--white)}
  body{position:relative;font-family:'Roboto',sans-serif;color:var(--text)}
  .site-header{position:absolute;top:0;left:0;width:1018px;height:93px}
  .brand{position:absolute;left:136px;top:24px;display:flex;align-items:center;gap:7px}
  .brand-dot{width:24px;height:24px;border-radius:50%;background:var(--sky)}
  .brand-name{font-family:'Roboto',sans-serif;font-weight:500;font-size:16px;line-height:19px;color:var(--sky)}
  .main-nav{position:absolute;left:370px;top:30px;display:flex;height:34px;background:var(--nav-bg)}
  .main-nav a{display:flex;align-items:center;justify-content:center;height:34px;font-size:13px;color:#666;text-decoration:none;border-right:1px solid #fff;white-space:nowrap}
  .main-nav a.active{background:var(--sky);color:var(--white)}
  .hero{position:absolute;top:93px;left:0;width:1018px;height:403px}
  .hero-photo{position:absolute;inset:0;background:linear-gradient(100deg,var(--green-1) 0%,#8fbf55 18%,var(--skin) 30%,#e8b3a2 50%,#d39a8a 70%,var(--green-2) 100%)}
  .hero-shade{position:absolute;left:601px;top:0;width:417px;height:403px;background:rgba(40,55,25,.55)}
  .quick-contact{position:absolute;left:664px;top:52px;width:218px;color:var(--white)}
  .quick-contact h2{font-family:'Open Sans',sans-serif;font-weight:300;font-size:17px;letter-spacing:.2px;margin-bottom:15px}
  .quick-contact h2 b{font-weight:700}
  .field{display:block;width:218px;border:2px solid rgba(255,255,255,.55);font-size:10.5px;color:var(--white);padding:6px 9px;margin-bottom:9px;height:28px}
  .field.comment{height:79px}
  .submit{display:block;margin:0 0 0 auto;width:94px;height:31px;background:var(--sky);color:var(--white);font-size:11px;text-align:center;line-height:31px}
  .contact-line{display:flex;justify-content:space-between;margin-top:21px;font-size:10.5px;padding-bottom:14px;border-bottom:1px solid rgba(255,255,255,.4);white-space:nowrap}
  .contact-line span{display:flex;align-items:center;gap:6px}
  .contact-line svg{flex-shrink:0}
  .about-band{position:absolute;top:496px;left:0;width:1018px;height:230px;background:var(--ink);text-align:center;color:#ddd}
  .about-band h2{font-family:'Open Sans',sans-serif;font-weight:400;font-size:16px;color:var(--white);margin-top:46px}
  .about-band h2 b{font-weight:700}
  .about-band p{width:760px;margin:10px auto 0;font-size:10.5px;line-height:15.2px}
  .btn{display:inline-block;width:79px;height:30px;line-height:30px;background:var(--btn);color:var(--white);font-size:11px;border-radius:2px;text-align:center}
  .about-band .btn{margin-top:19px}
  .services{position:absolute;top:726px;left:0;width:1018px;height:376px}
  .services h2{text-align:center;font-family:'Open Sans',sans-serif;font-weight:400;font-size:16px;color:#444;margin-top:37px}
  .services h2 b{font-weight:600;color:#222}
  .service-card{position:absolute;top:76px;width:227px;text-align:center}
  .service-photo{height:100px;border:1px solid #ddd;padding:4px;background:var(--white)}
  .service-photo div{width:100%;height:100%}
  .service-card h3{font-weight:500;font-size:12px;color:#555;margin-top:13px}
  .service-card p{font-size:10.5px;line-height:15.2px;color:var(--muted);margin-top:8px;padding:0 2px}
  .service-card .btn{margin-top:19px}
  .site-footer{position:absolute;top:1102px;left:0;width:1018px;height:98px;background:var(--sky);text-align:center;color:var(--white);font-size:10.5px}
  .footer-nav{margin-top:31px;display:flex;justify-content:center}
  .footer-nav a{color:var(--white);text-decoration:none;padding:0 14px;border-left:1px solid rgba(255,255,255,.8);line-height:12px;white-space:nowrap}
  .footer-nav a:first-child{border-left:none}
  .copyright{margin-top:10px}
</style>
</head>
<body>
  <header class="site-header">
    <div class="brand"><span class="brand-dot"></span><span class="brand-name">Meadowlane<br>Home Health</span></div>
    <nav class="main-nav">
      <a class="active" style="width:65px">Home</a>
      <a style="width:79px">About Us</a>
      <a style="width:75px">Services</a>
      <a style="width:86px">Resources</a>
      <a style="width:51px">FAQ</a>
      <a style="width:157px;border-right:none">Employment &amp; Contact</a>
    </nav>
  </header>

  <section class="hero">
    <div class="hero-photo" role="img" aria-label="Close-up of an elderly person's hand held by a caregiver's hand against a green background"></div>
    <div class="hero-shade"></div>
    <div class="quick-contact">
      <h2>QUICK <b>CONTACT</b></h2>
      <div class="field">Name *</div>
      <div class="field">E-mail*</div>
      <div class="field comment">Comment*</div>
      <div class="submit">Submit</div>
      <div class="contact-line">
        <span><svg width="12" height="12" viewBox="0 0 12 12"><rect width="12" height="12" rx="2" fill="#4bc8ef"/><path d="M3.5 2.5l1.5 0 .6 2-1 .8c.5 1.1 1.3 1.9 2.4 2.4l.8-1 2 .6v1.5c-3.6.2-6.5-2.7-6.3-6.3z" fill="#fff"/></svg>+800-555-0142</span>
        <span><svg width="12" height="10" viewBox="0 0 12 10"><rect width="12" height="10" rx="1" fill="#4bc8ef"/><path d="M1 1.5l5 4 5-4" stroke="#fff" stroke-width="1.2" fill="none"/></svg>help@meadowhh.com</span>
      </div>
    </div>
  </section>

  <section class="about-band">
    <h2>WE ARE CAREING <b>OLD AGED PEPOLE 24Hr</b></h2>
    <p>There are many variations of passages of Lorem Ipsum available, but the majority have suffered alteration in some form, by injected humour, or randomised words which don't look even slightly believable. If you are going to use a passage of Lorem Ipsum, you need to be sure there isn't anything Lorem Ipsum available, but the majority have suffered alteration in some form, by injected humour, or randomised words &nbsp;embarrassing hidden in the middle of text.<br>All the Lorem Ipsum generators on the anything embarrassing hidden</p>
    <span class="btn">Read More</span>
  </section>

  <section class="services">
    <h2><b>MAJOR</b> SERVICES</h2>
    <article class="service-card" style="left:136px">
      <div class="service-photo"><div role="img" aria-label="Young woman and elderly woman smiling together at home" style="background:linear-gradient(90deg,#c9b39a,#e9e4dc 60%,#b9c98a)"></div></div>
      <h3>24HR NURSING CARE</h3>
      <p>There are many variations of passages of Lorem Ipsum available, but the majority have suffered alteration in some form, by injected humour, randomised words which don't</p>
      <span class="btn">Read More</span>
    </article>
    <article class="service-card" style="left:396px">
      <div class="service-photo"><div role="img" aria-label="Elderly couple with a caregiver handing them a glass of water" style="background:linear-gradient(90deg,#7a6a8a,#c8b7a8 50%,#e8e2da)"></div></div>
      <h3>HOME CARE SERVICE</h3>
      <p>There are many variations of passages of Lorem Ipsum available, but the majority have suffered alteration in some form, by injected humour, randomised words which don't</p>
      <span class="btn">Read More</span>
    </article>
    <article class="service-card" style="left:655px">
      <div class="service-photo"><div role="img" aria-label="Nurse brushing an elderly woman's hair" style="background:linear-gradient(90deg,#8a9a4a,#e9e4dc 35%,#d8cfc4)"></div></div>
      <h3>RETIREMENT HOMES</h3>
      <p>There are many variations of passages of Lorem Ipsum available, but the majority have suffered alteration in some form, by injected humour, randomised words which don't</p>
      <span class="btn">Read More</span>
    </article>
  </section>

  <footer class="site-footer">
    <nav class="footer-nav">
      <a>Home</a><a>About Us</a><a>Services</a><a>Resources</a><a>FAQ</a><a>Employment &amp; Contact</a>
    </nav>
    <p class="copyright">Copyright © 2013 meadowlane care Allright Reserved</p>
  </footer>
</body>
</html>
```